One Page Sales Flyer for Wireless Survey- Computer Hardware

I want a designer to create a one page 4 color sales slick to be given to our sales team to sell to the end customers. I would like a visual picture of a heat map so zavvix "heat map wireless" to get an idea of how that image should look.

```html
<!DOCTYPE html>
<html lang="en">
<head>
<meta charset="utf-8">
<title>Wireless Site Surveys – Sales Flyer</title>
<link rel="stylesheet" href="https://fonts.googleapis.com/css2?family=Alfa+Slab+One&family=Montserrat:wght@500;600;700&display=swap">
<style>
:root{
  --blue:#11a3ea;
  --black:#000;
  --ink:#1e1e1e;
  --white:#fff;
  --stage:#ececec;
  --heat-warm:#f3a15f;
  --heat-mid:#f6cf6c;
  --heat-cool:#9cc3e6;
}
*{margin:0;padding:0;box-sizing:border-box}
html,body{width:1200px;height:1172px;overflow:hidden;background:var(--stage)}
.flyer{position:absolute;left:185px;top:0;width:830px;height:1172px;background:var(--white);font-family:"Montserrat",sans-serif;overflow:hidden}
.header{position:absolute;left:0;top:0;width:100%;height:246px;background:var(--blue);display:flex;align-items:center;justify-content:center}
.headline{font-family:"Alfa Slab One",serif;font-weight:400;color:var(--ink);font-size:47px;line-height:52px;text-align:center;letter-spacing:.5px;margin-top:8px}
.sidebar{position:absolute;left:47px;top:246px;width:318px;height:926px;background:var(--black);padding:38px 24px 0 24px;color:var(--white)}
.sidebar h2{color:var(--blue);font-size:18.5px;font-weight:600;line-height:23.5px}
.sidebar p,.sidebar li{font-size:13.4px;font-weight:500;line-height:17px;letter-spacing:.35px}
.sidebar section{margin-bottom:17px}
.reasons{list-style:none}
.reasons li{position:relative;padding-left:16px}
.reasons li::before{content:"";position:absolute;left:1px;top:6px;width:4px;height:4px;border-radius:50%;background:var(--blue)}
.contact{position:absolute;left:63px;top:1049px;width:286px;height:123px;background:var(--blue);padding:20px 0 0 16px;color:var(--white);font-weight:700}
.contact div{display:flex;align-items:center;gap:12px;font-size:19.5px;line-height:29px}
.contact .phone{font-size:29px;line-height:36px}
.contact svg{width:16px;height:16px;flex:none}
.heatmap{position:absolute;left:381px;top:263px;width:445px;height:213px;border:1px solid #8a8a8a;background:linear-gradient(90deg,var(--heat-mid),var(--heat-warm) 45%,var(--heat-mid) 75%,var(--heat-cool))}
.targets{position:absolute;left:400px;top:493px;width:406px}
.targets h2{font-family:"Alfa Slab One",serif;font-weight:400;color:var(--blue);font-size:31px;letter-spacing:3px;line-height:34px;margin-bottom:9px;white-space:nowrap}
.targets ul{list-style:none}
.targets li{height:33px;margin-bottom:11.2px;display:flex;align-items:center;justify-content:center;font-size:28px;font-weight:600;letter-spacing:.5px;line-height:1}
.targets li:nth-child(odd){background:var(--black);color:var(--blue)}
.targets li:nth-child(even){background:var(--blue);color:var(--white)}
.brand{position:absolute;left:431px;top:1018px;width:348px;height:90px;background:var(--black);display:flex;align-items:center;justify-content:center;gap:18px;color:var(--white);font-size:46px;font-weight:600;letter-spacing:2px}
.brand .mark{width:46px;height:46px;background:var(--blue)}
.footnote{position:absolute;left:441px;top:1158px;font-size:10px;font-weight:500;color:var(--ink)}
</style>
</head>
<body>
<main class="flyer">
  <header class="header">
    <h1 class="headline">INCREASE HARDWARE<br>AND SERVICES SPEND WITH<br>WIRELESS SITE SURVEYS</h1>
  </header>

  <aside class="sidebar">
    <section>
      <h2>What is a wireless site<br>survey or heat map?</h2>
      <p>A wireless site survey is a compilation of reports showing a visual representation of health of your wireless network. This does not only show how strong or weak a wireless signal is in any location it also helps aid in channel and placement to ensure maximum stable data rates are archived even where the single appears strong.</p>
    </section>
    <section>
      <h2>Why do customers need a<br>site survey?</h2>
      <p>Any variety of factors can contribute to an unhealthy wireless network (electrical, motors, materials used in construction, distance, neighboring wireless networks, etc.) and traditional methods that use only blueprints and a computer program to show signal strength have shown to be ineffective.</p>
    </section>
    <section>
      <h2>Why should they use you?</h2>
      <ul class="reasons">
        <li>42% of businesses report some issues with wireless connectivity and acknowledge its effect on the bottom line*</li>
        <li>Most of these problems are solved through either fine tuning the current equipment (managed services) or purchasing new equipment (incremental sales) of which you can provide both</li>
        <li>Being a one-stop shop for all your customer's IT needs prevents them from needing additional vendors</li>
        <li>The increase of IoT (Internet of things) and BYOD (Bring Your Own Device)</li>
      </ul>
    </section>
  </aside>

  <div class="contact">
    <div><svg viewBox="0 0 16 16"><rect x="1" y="3" width="14" height="10" fill="#fff"/><path d="M1 3l7 6 7-6" stroke="#11a3ea" stroke-width="1.5" fill="none"/></svg>www.trestlehq.com</div>
    <div><svg viewBox="0 0 16 16"><circle cx="8" cy="8" r="6.5" fill="none" stroke="#fff" stroke-width="1.5"/><path d="M1.5 8h13M8 1.5c-3 3.5-3 9.5 0 13M8 1.5c3 3.5 3 9.5 0 13" stroke="#fff" stroke-width="1.2" fill="none"/></svg>info@trestlehq.com</div>
    <div class="phone"><svg viewBox="0 0 16 16"><path d="M4 2c-3 3-3 9 1 12l2-2-2-2c-1-1-1-3 0-4l2-2-2-2z" fill="#fff"/></svg>555-014-2290</div>
  </div>

  <div class="heatmap" role="img" aria-label="Wireless signal heat map laid over an office floor plan"></div>

  <section class="targets">
    <h2>TARGET CUSTOMERS</h2>
    <ul>
      <li>DISTRIBUTORS</li>
      <li>WAREHOUSES</li>
      <li>SLED</li>
      <li>K-12</li>
      <li>MEDICAL / HOSPITALS</li>
      <li>ENTERPRISE F1000</li>
      <li>SPORTS VENUES</li>
      <li>STADIUMS</li>
      <li>HOTELS</li>
      <li>RETAIL STORES</li>
    </ul>
  </section>

  <div class="brand"><span class="mark"></span>TRESTLE</div>

  <p class="footnote">*Newswire Daily. “Connectivity in the Modern Enterprise”. June 2017</p>
</main>
</body>
</html>
```